Real Estate Investment Company Needs Business Card Design

TurnKeyMintHomes is a real estate investment company that primarily deals directly with homeowners looking to sell their homes in "as is" condition as quick as possible. We give this seller cash and close on their nightmare of a property in just a matter of days.

Our logo is attached - (please keep logo in tact, use as is)

Industry/Entity Type

Real Estate

Contact Information for Business Card

The design should invoke trust & professionalism. The person holding the card should feel rest assured that we are the right company to work with.

Font styles to use
Sans Serif

Requirements
Must have
• Card must include "Call us today for a fair offer on your property so you can move on with your life!"
Nice to have
• If possible, include this either on front or back (you can use your own formatting, below is just the text)
• "
• No Realtor Commissions
• No Repairs To Deal With
• No Closing Costs "

```html
<!DOCTYPE html>
<html lang="en">
<head>
<meta charset="utf-8">
<title>TurnKeyMintHomes Business Cards</title>
<link href="https://fonts.googleapis.com/css2?family=Open+Sans:wght@400;600;700&display=swap" rel="stylesheet">
<style>
  :root {
    --brand-blue: #1e8fe0;
    --brand-dark: #2b2b2b;
    --ink: #333333;
    --muted: #666666;
    --rule: #cfcfcf;
    --paper: #ffffff;
    --stage: #e9e9e9;
  }
  * { margin: 0; padding: 0; box-sizing: border-box; }
  html, body { width: 1200px; height: 948px; overflow: hidden; }
  body {
    background: var(--stage);
    font-family: "Open Sans", Arial, sans-serif;
    color: var(--ink);
    display: flex;
    align-items: center;
    justify-content: center;
    gap: 40px;
  }
  .card {
    position: relative;
    width: 540px;
    height: 309px;
    background: var(--paper);
    box-shadow: 0 6px 18px rgba(0,0,0,0.15);
    overflow: hidden;
  }
  .card-front .swoosh { position: absolute; left: 0; top: 0; width: 540px; height: 309px; }
  .wordmark {
    display: flex;
    align-items: center;
    gap: 10px;
    font-weight: 700;
    color: var(--brand-blue);
    letter-spacing: -0.5px;
    white-space: nowrap;
  }
  .wordmark .mark-dot {
    width: 30px; height: 30px;
    border-radius: 50%;
    background: var(--brand-blue);
    flex: none;
  }
  .card-front .wordmark {
    position: absolute;
    left: 150px; top: 52px;
    font-size: 30px;
  }
  .card-front .divider-h {
    position: absolute;
    left: 170px; right: 36px; top: 128px;
    border-top: 1px solid var(--rule);
  }
  .contact-list {
    position: absolute;
    left: 170px; top: 146px;
    list-style: none;
    font-size: 12.5px;
    line-height: 22px;
    color: var(--ink);
  }
  .contact-list li { display: flex; align-items: center; gap: 8px; }
  .contact-list svg { width: 13px; height: 13px; flex: none; }
  .contact-list .address { padding-left: 21px; }
  .divider-v {
    position: absolute;
    left: 372px; top: 146px;
    height: 110px;
    border-left: 1px solid var(--rule);
  }
  .person {
    position: absolute;
    left: 388px; top: 146px;
  }
  .person .name { font-size: 15px; font-weight: 700; color: var(--brand-blue); }
  .person .title { font-size: 12.5px; font-weight: 600; color: var(--brand-dark); }

  .card-back {
    display: flex;
    flex-direction: column;
    align-items: center;
    justify-content: center;
    gap: 20px;
  }
  .card-back .wordmark { font-size: 34px; }
  .benefits {
    list-style: none;
    display: flex;
    flex-wrap: wrap;
    justify-content: center;
    gap: 6px 22px;
    width: 380px;
    font-size: 13.5px;
    color: var(--ink);
  }
  .benefits li { display: flex; align-items: center; gap: 7px; }
  .benefits li::before {
    content: "";
    width: 7px; height: 7px;
    background: var(--brand-blue);
  }
  .call-to-action {
    width: 400px;
    padding-top: 14px;
    border-top: 1px solid var(--rule);
    font-size: 12.5px;
    line-height: 19px;
    font-weight: 600;
    color: var(--brand-dark);
    text-align: center;
  }
</style>
</head>
<body>

<section class="card card-front" aria-label="Card front">
  <svg class="swoosh" viewBox="0 0 540 309" aria-hidden="true">
    <path d="M0 0 H70 C30 70 40 160 150 309 H0 Z" fill="var(--brand-blue)"/>
    <path d="M0 0 H58 C22 70 28 160 128 309 H0 Z" fill="var(--brand-dark)"/>
    <path d="M0 0 H46 C12 70 14 160 104 309 H0 Z" fill="var(--paper)"/>
    <path d="M0 0 H30 C4 80 -2 170 70 309 H0 Z" fill="var(--brand-blue)"/>
  </svg>

  <div class="wordmark">
    <span class="wordmark-name">TurnKeyMintHomes</span>
    <span class="mark-dot"></span>
  </div>

  <div class="divider-h"></div>

  <ul class="contact-list">
    <li>
      <svg viewBox="0 0 16 16"><circle cx="8" cy="8" r="8" fill="var(--brand-dark)"/><path d="M5 4.5l1.5-.5 1 2-1 .8c.4 1 1.2 1.8 2.2 2.2l.8-1 2 1-.5 1.5c-3 .3-6.3-3-6-6z" fill="#fff"/></svg>
      <span>012-345-6789</span>
    </li>
    <li>
      <svg viewBox="0 0 16 16"><circle cx="8" cy="8" r="8" fill="var(--brand-dark)"/><rect x="4" y="4.5" width="8" height="7" rx="1" fill="#fff"/><path d="M4.5 5.5h7v1h-7z" fill="var(--brand-dark)"/></svg>
      <span>012-345-6789</span>
    </li>
    <li>
      <svg viewBox="0 0 16 16"><circle cx="8" cy="8" r="8" fill="var(--brand-dark)"/><rect x="4" y="5" width="8" height="6" fill="#fff"/><path d="M4 5l4 3.5L12 5" fill="none" stroke="var(--brand-dark)" stroke-width="1"/></svg>
      <span>info@turnkeyminthomes.com</span>
    </li>
    <li>
      <svg viewBox="0 0 16 16"><circle cx="8" cy="8" r="8" fill="var(--brand-dark)"/><circle cx="8" cy="8" r="4" fill="none" stroke="#fff" stroke-width="1"/><path d="M4 8h8M8 4c-2 2.5-2 5.5 0 8M8 4c2 2.5 2 5.5 0 8" fill="none" stroke="#fff" stroke-width="0.8"/></svg>
      <span>www.turnkeyminthomes.com</span>
    </li>
    <li class="address">Street Name, City Name</li>
    <li class="address">Zipcode-01234</li>
  </ul>

  <div class="divider-v"></div>

  <div class="person">
    <p class="name">Your Name</p>
    <p class="title">Title</p>
  </div>
</section>

<section class="card card-back" aria-label="Card back">
  <div class="wordmark">
    <span class="wordmark-name">TurnKeyMintHomes</span>
    <span class="mark-dot"></span>
  </div>
  <ul class="benefits">
    <li>No Realtor Commisions</li>
    <li>No Repairs To Deal With</li>
    <li>No Closing Costs</li>
  </ul>
  <p class="call-to-action">Call us today for a fair offer on your property so you can move on with your life!</p>
</section>

</body>
</html>
```